carpet bamboo timber flooring flyer EVERYONE NOTE WE SELL CARPET AND VINYL AS WELL PICTURES TBC

make a A4 Flyer to send to builder real estate companies customers insurance ect ect in the profession5 folder our logo is number 5
we are calling all builders ect in our area then following up with flyer at the same time to try to get projects or customers to quote on like flood damage rental properties new home builds , tenders ect

we will need to discuss with pictures go where ect but you have the idea what im after

Target Market(s)

builders insurance brokers customers builders developers

Industry/Entity Type

Flooring

Font styles to use
Decorative

Colors
f37122
fabb94
fee18a
faa54b

Requirements
Must have
• class clear vision high impact call to action informative
Nice to have
• like to see images on our showroom and recent jobs logos of our main brands

```html
<!DOCTYPE html>
<html lang="en">
<head>
<meta charset="utf-8">
<title>Keystone Floors – A4 Flyer</title>
<link href="https://fonts.googleapis.com/css2?family=Ubuntu:wght@400;500;700&family=Open+Sans:wght@400;600&display=swap" rel="stylesheet">
<style>
:root{
  --bg:#e4e1dc;
  --orange:#f37122;
  --amber:#faa54b;
  --yellow:#fdc82f;
  --cream:#fee18a;
  --brown:#3a2414;
  --brown-mid:#5a3a1f;
  --wood-a:#8a5a2b;
  --wood-b:#b07a3e;
  --wood-c:#6b4220;
  --white:#ffffff;
}
*{box-sizing:border-box;margin:0;padding:0}
html,body{width:1200px;height:768px;overflow:hidden}
body{background:var(--bg);position:relative;font-family:"Open Sans",sans-serif}
.flyer{position:absolute;top:48px;width:476px;height:672px;background:linear-gradient(180deg,#9a6732,var(--wood-a) 50%,#7a4c24 80%,var(--wood-c));overflow:hidden;box-shadow:0 4px 14px rgba(0,0,0,.25)}
.flyer--front{left:84px}
.flyer--back{left:640px}
.header{position:absolute;left:0;top:0;width:100%;height:70px;background:var(--white);border-top:4px solid var(--yellow);z-index:2}
.brand{position:absolute;left:34px;top:11px;display:flex;align-items:center;gap:8px}
.brand-mark{width:42px;height:42px;background:var(--orange);border-radius:4px}
.brand-name{font-family:"Ubuntu",sans-serif;font-weight:500;font-size:21px;line-height:19px;color:var(--orange);width:120px}
.cta{position:absolute;right:28px;top:4px;width:140px;height:52px;background:var(--brown);border-radius:3px;color:var(--white);font-family:"Ubuntu",sans-serif;font-weight:500;padding:6px 10px;line-height:20px}
.cta-label{font-size:17px;display:block}
.cta-phone{font-size:19px;display:block}
.photo{position:absolute}
.hero-front{left:0;top:70px;width:100%;height:200px;background:
  radial-gradient(ellipse 60% 40% at 35% 55%,rgba(230,230,228,.85),rgba(230,230,228,0) 70%),
  radial-gradient(ellipse 50% 45% at 78% 25%,rgba(214,226,232,.9),rgba(214,226,232,0) 75%),
  linear-gradient(180deg,#6e5e50 0%,#8f8174 28%,#5b3a22 55%,#7a4a24 80%,rgba(138,90,43,0) 100%)}
.headline{position:absolute;left:0;top:161px;width:100%;text-align:center;font-family:"Ubuntu",sans-serif;font-weight:700;color:var(--white);font-size:24px;line-height:29px;text-shadow:0 1px 3px rgba(0,0,0,.7);z-index:1}
.room-row{position:absolute;left:29px;top:229px;width:421px;height:99px;background:var(--white);padding:3px;display:flex;gap:3px}
.room-row .tile{flex:1;position:relative;height:100%}
.welcome{position:absolute;left:0;top:344px;width:100%;text-align:center;font-family:"Ubuntu",sans-serif;font-weight:400;color:var(--white);font-size:21px;line-height:25px}
.welcome b{font-weight:500}
.product-row{position:absolute;left:33px;top:423px;width:412px;height:137px;display:flex;gap:8px}
.product{flex:1;position:relative;border:2px solid var(--white)}
.product .photo{inset:0}
.caption{position:absolute;left:0;bottom:0;width:100%;height:24px;background:rgba(58,36,20,.88);color:var(--white);font-size:13px;text-align:center;line-height:24px;white-space:nowrap}
.assoc-band{position:absolute;left:0;top:566px;width:100%;height:18px;background:var(--yellow);text-align:center;font-size:13px;line-height:18px;color:var(--brown)}
.partners{position:absolute;left:0;top:584px;width:100%;height:52px;background:var(--white);display:flex;align-items:center;justify-content:center;gap:7px}
.partner{width:52px;height:30px}
.footer{position:absolute;left:0;bottom:0;width:100%;background:var(--brown);color:var(--white);font-size:10px}
.footer-front{height:36px;display:flex;align-items:center;padding:0 14px;gap:10px}
.footer-col{display:flex;flex-direction:column;gap:3px}
.footer-item{display:flex;align-items:center;gap:5px;white-space:nowrap}
.divider{width:2px;height:36px;background:var(--yellow);transform:skewX(-20deg)}
.icon{width:10px;height:10px;flex:none}
.hero-back{left:0;top:70px;width:100%;height:262px;background:
  radial-gradient(ellipse 30% 22% at 85% 12%,rgba(70,110,60,.9),rgba(70,110,60,0) 80%),
  radial-gradient(ellipse 20% 30% at 52% 26%,rgba(212,60,70,.85),rgba(212,60,70,0) 80%),
  radial-gradient(ellipse 45% 18% at 66% 52%,rgba(48,72,150,.95),rgba(48,72,150,0) 85%),
  radial-gradient(ellipse 28% 34% at 18% 48%,rgba(236,232,222,.95),rgba(236,232,222,0) 80%),
  radial-gradient(ellipse 60% 22% at 60% 76%,rgba(120,112,104,.9),rgba(120,112,104,0) 85%),
  linear-gradient(180deg,#8fb4dc 0%,#c7d8e8 28%,#b9b2a8 55%,#5e564f 80%,#7a4c24 100%)}
.grid{position:absolute;left:38px;top:314px;width:400px;height:254px;display:grid;grid-template-columns:192px 192px;grid-template-rows:121px 121px;column-gap:16px;row-gap:12px}
.cell{position:relative;border:3px solid var(--yellow)}
.cell .photo{inset:0}
.cell .caption{background:rgba(90,58,31,.8);height:22px;line-height:22px;font-size:10.5px}
.about-tab{position:absolute;left:180px;top:580px;width:116px;height:16px;background:var(--yellow);color:var(--white);font-size:12px;text-align:center;line-height:16px;clip-path:polygon(8% 0,92% 0,100% 100%,0 100%);z-index:1}
.about-text{position:absolute;left:36px;top:599px;width:404px;color:var(--white);font-size:7.2px;line-height:9.6px;text-align:center}
.about-band{position:absolute;left:0;top:596px;width:100%;height:54px;background:rgba(58,36,20,.55)}
.footer-back{height:22px;display:flex;align-items:center;justify-content:center;gap:14px;font-size:10.5px}
</style>
</head>
<body>

<svg width="0" height="0" style="position:absolute">
  <symbol id="i-phone" viewBox="0 0 10 10"><circle cx="5" cy="5" r="4.3" fill="none" stroke="#fdc82f" stroke-width="1"/><path d="M3.4 2.8l1 .9-.5.7c.4.8.9 1.3 1.6 1.6l.7-.5.9 1-.6.7C4.8 7 3 5.2 2.8 3.4z" fill="#fdc82f"/></symbol>
  <symbol id="i-pin" viewBox="0 0 10 10"><path d="M5 .8a3 3 0 0 1 3 3c0 2.2-3 5.4-3 5.4S2 6 2 3.8a3 3 0 0 1 3-3z" fill="#fdc82f"/><circle cx="5" cy="3.8" r="1.1" fill="#3a2414"/></symbol>
  <symbol id="i-mail" viewBox="0 0 10 10"><rect x=".8" y="2" width="8.4" height="6" fill="none" stroke="#fdc82f" stroke-width="1"/><path d="M.8 2L5 5.6 9.2 2" fill="none" stroke="#fdc82f" stroke-width="1"/></symbol>
  <symbol id="i-web" viewBox="0 0 10 10"><circle cx="5" cy="5" r="4" fill="none" stroke="#fdc82f" stroke-width="1"/><path d="M1 5h8M5 1c-2 2.5-2 5.5 0 8M5 1c2 2.5 2 5.5 0 8" fill="none" stroke="#fdc82f" stroke-width=".8"/></symbol>
</svg>

<section class="flyer flyer--front">
  <div class="photo hero-front" role="img" aria-label="Modern lounge with sofa, coffee table and marble feature wall on dark timber floor"></div>

  <header class="header">
    <div class="brand"><span class="brand-mark"></span><span class="brand-name">Keystone Floors</span></div>
    <div class="cta"><span class="cta-label">CALL US NOW</span><span class="cta-phone">0400 555 018</span></div>
  </header>

  <h1 class="headline">Flood Damage? Rental Properties?<br>New Home Builds? Tenders Etc?</h1>

  <div class="room-row">
    <div class="photo tile" style="background:radial-gradient(ellipse at 55% 75%,#e9d6d0,rgba(233,214,208,0) 60%),linear-gradient(160deg,#c8324a,#b52840 45%,#d8c3bc)" role="img" aria-label="Bedroom with red feature wallpaper and carpet"></div>
    <div class="photo tile" style="background:radial-gradient(ellipse at 60% 70%,#f7f3ec,rgba(247,243,236,0) 60%),linear-gradient(170deg,#e4ddcf,#c9bba5 60%,#b8a88f)" role="img" aria-label="Bright bedroom with cream carpet"></div>
    <div class="photo tile" style="background:radial-gradient(ellipse at 40% 55%,#f4f0ea,rgba(244,240,234,0) 45%),linear-gradient(180deg,#d9cdb8,#8a6a55 45%,#6e1d35 75%,#561428)" role="img" aria-label="Living room with burgundy carpet and white armchair"></div>
    <div class="photo tile" style="background:radial-gradient(ellipse at 70% 40%,#4d4a46,rgba(77,74,70,0) 50%),linear-gradient(160deg,#dfe3e2,#a8aba9 55%,#6e6e6a)" role="img" aria-label="Modern living area with grey carpet"></div>
  </div>

  <p class="welcome">WELCOME TO <b>KEYSTONE FLOORS</b>,<br>THE SPECIALIST IN <b>FLOORING IN ADELAIDE</b><br>CARPET VINYL ECT</p>

  <div class="product-row">
    <div class="product"><div class="photo" style="background:radial-gradient(ellipse at 30% 40%,#ece5d6,rgba(236,229,214,0) 45%),linear-gradient(180deg,#5c4a3a,#8a5a35 45%,#a05a28 75%,#7a3f1a)" role="img" aria-label="Dining area with timber flooring"></div><span class="caption">Timber Flooring</span></div>
    <div class="product"><div class="photo" style="background:radial-gradient(ellipse at 50% 45%,#2a2420,rgba(42,36,32,0) 40%),linear-gradient(180deg,#c9c7b8,#8c7b5f 50%,#6b4d2e)" role="img" aria-label="Lounge with bamboo flooring"></div><span class="caption">Bamboo Flooring</span></div>
    <div class="product"><div class="photo" style="background:radial-gradient(ellipse at 40% 45%,#a5581f,rgba(165,88,31,0) 55%),linear-gradient(180deg,#efe4cf,#c88a4a 45%,#9a5a2a)" role="img" aria-label="Kitchen with laminate flooring"></div><span class="caption">Laminate Flooring</span></div>
  </div>

  <div class="assoc-band">Proudly Associated With</div>
  <div class="partners">
    <span class="partner" style="background:#1f3f8f"></span>
    <span class="partner" style="background:#2b2b2b;width:60px"></span>
    <span class="partner" style="background:#f2c500;width:30px"></span>
    <span class="partner" style="background:#f08a24;width:40px"></span>
    <span class="partner" style="background:#3a2a7a"></span>
    <span class="partner" style="background:#d21d2b"></span>
    <span class="partner" style="background:#111111"></span>
    <span class="partner" style="background:#2c62b0"></span>
  </div>

  <footer class="footer footer-front">
    <div class="footer-col">
      <span class="footer-item"><svg class="icon"><use href="#i-pin"/></svg>48 Harbour Road Westbrook P/C5099</span>
      <span class="footer-item"><svg class="icon"><use href="#i-mail"/></svg>hello@keystonefloors.example</span>
    </div>
    <span class="divider"></span>
    <div class="footer-col">
      <span class="footer-item"><svg class="icon"><use href="#i-phone"/></svg>(08) 5550 1742</span>
      <span class="footer-item"><svg class="icon"><use href="#i-phone"/></svg>0400 555 018</span>
    </div>
    <span class="divider"></span>
    <span class="footer-item" style="font-size:8.5px"><svg class="icon"><use href="#i-web"/></svg>www.keystonefloors.example</span>
  </footer>
</section>

<section class="flyer flyer--back">
  <div class="photo hero-back" role="img" aria-label="Showroom shopfront with blue carpet and vinyl signage, red feather flags and parked cars"></div>

  <header class="header">
    <div class="brand"><span class="brand-mark"></span><span class="brand-name">Keystone Floors</span></div>
    <div class="cta"><span class="cta-label">CALL US NOW</span><span class="cta-phone">0400 555 018</span></div>
  </header>

  <div class="grid">
    <div class="cell"><div class="photo" style="background:radial-gradient(ellipse at 45% 40%,#4a2a1c,rgba(74,42,28,0) 45%),linear-gradient(180deg,#d7c9b4,#9a5a30 50%,#6e3418)" role="img" aria-label="Study with leather chair on timber flooring"></div><span class="caption">Timber Flooring in Adelaide</span></div>
    <div class="cell"><div class="photo" style="background:radial-gradient(ellipse at 45% 40%,#ddd6c8,rgba(221,214,200,0) 50%),linear-gradient(180deg,#c9c0b0,#b58448 55%,#a06a30)" role="img" aria-label="Lounge with bamboo flooring"></div><span class="caption">Bamboo Flooring in Adelaide</span></div>
    <div class="cell"><div class="photo" style="background:radial-gradient(ellipse at 35% 35%,#f0ece6,rgba(240,236,230,0) 50%),linear-gradient(180deg,#cbc3b7,#d9d3c8 50%,#b9ad9c)" role="img" aria-label="Living room with pale laminate floating floor"></div><span class="caption">Laminate Floating Floors in Adelaide</span></div>
    <div class="cell"><div class="photo" style="background:radial-gradient(ellipse at 30% 45%,#b8283a,rgba(184,40,58,0) 30%),radial-gradient(ellipse at 55% 40%,#f1e6d6,rgba(241,230,214,0) 45%),linear-gradient(180deg,#4a3a30,#c08a4c 50%,#d49c5a)" role="img" aria-label="Living room with sanded and polished floor"></div><span class="caption">Floor Sanding &amp; Polishing Adelaide</span></div>
  </div>

  <div class="about-band"></div>
  <div class="about-tab">About Us</div>
  <p class="about-text">Keystone Floors was established in 1980 and service the whole of South Australia, from Seacliff Point to Northhaven. As a company, we are extremely passionate about flooring and are committed to delivering exceptional result to our valued customers. We strive to educate our customers on both the positives and negatives of all our flooring options, so they can make a well-informed decision. When you leave our showrooms, you will be armed with all the knowledge to make the right flooring choice for the area in your home and the product concerned.</p>

  <footer class="footer footer-back">
    <span class="footer-item"><svg class="icon"><use href="#i-mail"/></svg>hello@keystonefloors.example</span>
    <span class="divider" style="height:22px"></span>
    <span class="footer-item"><svg class="icon"><use href="#i-phone"/></svg>(08) 5550 1742</span>
    <span class="footer-item"><svg class="icon"><use href="#i-phone"/></svg>0400 555 018</span>
  </footer>
</section>

</body>
</html>
```